Security Officer Training Certifications POSTCARD

We need Post Card Design
-Front and Back
-In Compliance with TORLEN HUB for upload!
-For Oversized and Jumbo Size Cards (torlen hubs)
Our Company:
www.ashworthmaplebrookinstitute.org (FOR IDEAS)
We provide Corporate Security Officer/Criminal Justice/Police Tactics Training for Private Companies that have a security department and officers.
We provide:
Handcuffing certifications
Pepper Spray
Compliance Training
Instructor Training
California Guard Card
Our Card to display powerful image for a Security Officer Department
Traits in Pic and Deigns
VALUE
COMPETITIVE EDGE
PROFESSIONAL GROWTH
QUALITY
PROFICIENT/EFFECTIVE SECURITY OFFICERS
TACTICAL OFFICERS
PROFESSIONALISM
EXPERTS
INDUSTRY LEADERS
READINESS
FRONT DESIGN TO BE VERY CATCH AND ATTRACTIVE!
-Please put the images of lawn enforcement, security guards, public safety department in the FRONT
BACK OF THE CARD DESIGN
-Please put our Services/Menu, CREATIVE and CATCHY, in columns and with vivid colors.

```html
<!DOCTYPE html>
<html lang="en">
<head>
<meta charset="utf-8">
<title>Security Officer Training Postcard</title>
<link rel="stylesheet" href="https://fonts.googleapis.com/css2?family=Tinos:wght@400;700&display=swap">
<style>
:root{
  --navy:#241f6e;
  --indigo:#3a33a3;
  --gold:#f9d46b;
  --gold-text:#f7cf55;
  --ink:#1c1c2e;
  --white:#ffffff;
  --page:#e9e9ec;
}
*{box-sizing:border-box;margin:0;padding:0}
html,body{width:1200px;height:1024px;overflow:hidden;background:var(--page)}
body{position:relative;font-family:"Tinos","Times New Roman",serif;color:var(--white)}
.card{position:absolute;left:226px;width:747px;height:491px;overflow:hidden;background:var(--white);box-shadow:0 2px 8px rgba(0,0,0,.25)}
.card--front{top:14px}
.card--back{top:523px}
.abs{position:absolute}
.panel{position:absolute;left:0;top:0;bottom:0;background:radial-gradient(ellipse at 70% 55%,var(--indigo) 0%,var(--navy) 75%)}
.card--front .panel{width:403px}
.card--back .panel{width:406px}
.title{left:0;width:380px;text-align:center;font-size:26px;line-height:27px;top:22px}
.title-accent{left:0;width:380px;text-align:center;top:78px;font-size:23px;font-weight:700;color:var(--gold-text);letter-spacing:1px}
.question{left:20px;top:114px;font-size:14px;color:var(--gold-text)}
.intro{left:20px;top:131px;width:340px;font-size:10.5px;line-height:13px}
.programs{top:173px;font-size:10.5px;line-height:13px;list-style:none}
.programs--a{left:20px;width:140px}
.programs--b{left:166px;width:190px}
.offer-box{left:27px;top:243px;width:298px;height:192px;background:var(--gold);border-radius:30px}
.offer{position:absolute;left:18px;width:270px;height:48px}
.offer-mark{position:absolute;left:0;top:0;width:48px;height:48px;background:#3d3a4f;border:2px solid #fff}
.offer-text{position:absolute;left:57px;top:2px;font-size:8.5px;line-height:10.5px;color:var(--ink)}
.offer-text b{display:block}
.offer-text span{display:block;padding-left:6px}
.photo{position:absolute}
.photo--guard{left:403px;top:0;width:344px;height:245px;background:linear-gradient(135deg,#b9b0a8 0%,#8b7b70 40%,#2a2e38 100%)}
.stripe{left:400px;top:245px;width:347px;height:9px;background:var(--gold)}
.photo--gavel{left:400px;top:254px;width:181px;height:197px;background:linear-gradient(160deg,#d8cdb9 0%,#7a4a2c 55%,#3a1f12 100%)}
.photo--patrol{left:585px;top:254px;width:162px;height:197px;background:linear-gradient(160deg,#bcc1c9 0%,#5d6373 50%,#1d2230 100%)}
.badge{left:338px;top:172px;width:110px;height:112px;border-radius:50%;background:radial-gradient(circle at 40% 35%,#ffffff 0%,#c9ccd2 45%,#8d929c 100%);border:3px solid #d9b75a}
.footer{position:absolute;left:0;right:0;bottom:0;background:var(--gold);color:var(--ink);font-size:10.5px}
.card--front .footer{height:40px}
.card--back .footer{height:51px}
.footer-item{position:absolute;top:50%;transform:translateY(-50%);display:flex;align-items:center;gap:10px}
.footer-phone{left:26px;font-weight:700}
.footer-web{left:272px;gap:20px}
.footer-address{left:575px;gap:14px;line-height:12px}
.heading{left:23px;top:24px;font-size:20px}
.services{left:22px;top:54px;list-style:none;font-size:12.5px}
.services li{display:flex;align-items:center;gap:9px;height:28.5px}
.photo--officer{left:209px;top:59px;width:174px;height:112px;border:1px solid #c8c4e8;background:linear-gradient(135deg,#5d7a3f 0%,#a7b38c 45%,#dfe1e6 70%,#4a4f58 100%)}
.section-title{left:25px;top:216px;font-size:19px;color:var(--gold-text)}
.sched{font-size:11.5px;line-height:14.5px}
.sched-head{font-size:14px;color:var(--gold-text);line-height:16px}
.fees{left:188px;top:308px}
.stamp{left:627px;top:20px;width:100px;height:100px;border:1.5px solid #111}
.rule{left:466px;width:249px;height:1px;background:#444}
</style>
</head>
<body>

<section class="card card--front" aria-label="Postcard front">
  <div class="panel"></div>
  <div class="photo photo--guard" role="img" aria-label="Photo of a security officer in cap and sunglasses speaking on a radio"></div>
  <div class="abs stripe"></div>
  <div class="photo photo--gavel" role="img" aria-label="Photo of a judge's gavel, scales and law books"></div>
  <div class="photo photo--patrol" role="img" aria-label="Photo of a uniformed officer on patrol in a busy street"></div>
  <div class="abs badge" role="img" aria-label="Training institute badge"></div>

  <h1 class="abs title" style="font-weight:400">Security Guard Training in<br>Los Angeles California</h1>
  <div class="abs title-accent">GUARD CARD SPECIALISTS</div>
  <h2 class="abs question" style="font-weight:400">What’s the right Program for me?</h2>
  <p class="abs intro">Choose from our wide range of Certifications, Credentials, &amp; licensing packages depending on the type of security jobs and pay you are interested in:</p>
  <ul class="abs programs programs--a">
    <li>*Security Officer Academy</li>
    <li>*Certified Firearms Officer</li>
    <li>*Certified Protection Officer (Guard Card)</li>
  </ul>
  <ul class="abs programs programs--b">
    <li>*Loss Prevention Agent</li>
    <li>*Campus Security Officer (CSO)</li>
    <li>*Handcuffing Tactics w/Guard Card</li>
  </ul>

  <div class="abs offer-box">
    <div class="offer" style="top:11px">
      <div class="offer-mark" style="background:#e8e8ea"></div>
      <p class="offer-text"><b>Become a Certified Firearms Officer (CFO)<br>for positions as an armed officer!</b><span>California Guard Card license!</span><span>Exposed Firearms License!</span></p>
    </div>
    <div class="offer" style="top:70px">
      <div class="offer-mark" style="background:#d3d3d6"></div>
      <p class="offer-text"><b>Become a Certified Firearms Officer (CFO)<br>for positions as an armed officer!</b><span>California Guard Card license!</span><span>Exposed Firearms License!</span></p>
    </div>
    <div class="offer" style="top:130px">
      <div class="offer-mark" style="background:#1f2433"></div>
      <p class="offer-text"><b>This basic program allows you entry level positions<br>in security!</b><span>California Guard Card License!</span></p>
    </div>
  </div>

  <div class="footer">
    <div class="footer-item footer-phone">
      <svg width="14" height="14" viewBox="0 0 24 24"><path fill="#fff" d="M6.6 10.8a15.1 15.1 0 006.6 6.6l2.2-2.2c.3-.3.7-.4 1-.2 1.1.4 2.3.6 3.6.6.6 0 1 .4 1 1V20c0 .6-.4 1-1 1A17 17 0 013 4c0-.6.4-1 1-1h3.5c.6 0 1 .4 1 1 0 1.3.2 2.5.6 3.6.1.3 0 .7-.2 1z"/></svg>
      (555) 014-2290
    </div>
    <div class="footer-item footer-web">
      <svg width="18" height="18" viewBox="0 0 24 24" fill="none" stroke="#fff" stroke-width="1.6"><circle cx="12" cy="12" r="10"/><ellipse cx="12" cy="12" rx="4.5" ry="10"/><path d="M2 12h20M4 7h16M4 17h16"/></svg>
      www.ashworthmaplebrookinstitute.org
    </div>
    <div class="footer-item footer-address">
      <svg width="20" height="18" viewBox="0 0 24 22"><path fill="#fff" d="M12 1L1 11h3v10h6v-6h4v6h6V11h3z"/></svg>
      <span>2810 W. Alder Crest Ave,<br>#214 Fairmont, CA 90000</span>
    </div>
  </div>
</section>

<section class="card card--back" aria-label="Postcard back">
  <div class="panel"></div>
  <h2 class="abs heading" style="font-weight:400">WE PROVIDE:</h2>
  <ul class="abs services">
    <li><svg width="20" height="20" viewBox="0 0 20 20"><circle cx="10" cy="10" r="9.5" fill="var(--gold)"/><circle cx="7" cy="12" r="3" fill="none" stroke="#fff" stroke-width="1.5"/><circle cx="13" cy="12" r="3" fill="none" stroke="#fff" stroke-width="1.5"/><path d="M8 5h4" stroke="#fff" stroke-width="1.5"/></svg>Handcuffing certifications</li>
    <li><svg width="20" height="20" viewBox="0 0 20 20"><circle cx="10" cy="10" r="9.5" fill="var(--gold)"/><rect x="8" y="7" width="4" height="8" rx="1" fill="#fff"/><rect x="9" y="4.5" width="2" height="2" fill="#fff"/></svg>Pepper Spray</li>
    <li><svg width="20" height="20" viewBox="0 0 20 20"><circle cx="10" cy="10" r="9.5" fill="var(--gold)"/><circle cx="10" cy="10" r="5" fill="none" stroke="#fff" stroke-width="1.5"/><circle cx="10" cy="10" r="1.8" fill="#fff"/></svg>Compliance Training</li>
    <li><svg width="20" height="20" viewBox="0 0 20 20"><circle cx="10" cy="10" r="9.5" fill="var(--gold)"/><circle cx="8" cy="6" r="2" fill="#fff"/><path d="M6 15v-5h4v5M11 8h4v4h-4" fill="#fff"/></svg>Instructor Training</li>
    <li><svg width="20" height="20" viewBox="0 0 20 20"><circle cx="10" cy="10" r="9.5" fill="var(--gold)"/><path d="M10 3.5l5 2v4c0 3-2.2 5.3-5 6.5-2.8-1.2-5-3.5-5-6.5v-4z" fill="#fff"/><path d="M7.5 10l2 2 3.2-3.5" fill="none" stroke="var(--gold)" stroke-width="1.5"/></svg>California Guard Card</li>
  </ul>
  <div class="photo photo--officer" role="img" aria-label="Photo of a uniformed officer speaking with a driver at a car window"></div>

  <h2 class="abs section-title" style="font-weight:400">SCHEDULES</h2>
  <p class="abs sched" style="left:25px;top:248px">California Guard Card Every FRIDAYS 8am-5pm</p>
  <div class="abs sched" style="left:25px;top:277px">
    <p class="sched-head">Every 3rd Monday</p>
    <p>First Aid CPR 8am-9am</p>
    <p>Pepper Spray&nbsp; 9am -10am</p>
    <p>Handcuffing&nbsp; 10am-12pm</p>
  </div>
  <div class="abs sched" style="left:25px;top:351px">
    <p class="sched-head">Every 3rd Tuesday</p>
    <p>Exposed Firearms Training</p>
    <p>Day 1 Tuesday 8am-5pm</p>
    <p>Day 2 same Thursday 8am-2pm</p>
  </div>
  <div class="abs sched fees">
    <p class="sched-head">State fees: Pay as you go, own time!</p>
    <p>California Guard Card State fee&nbsp; 50</p>
    <p>Firearms Permits State fee&nbsp; 80</p>
    <p>National Aid Society Permit fee&nbsp; 27</p>
    <p>Range fees (50 bullets/gun use) 50</p>
    <p>Livescan Guard Card 69</p>
    <p>Livescan Guar Card &amp; Firearms 107</p>
  </div>

  <div class="abs stamp"></div>
  <div class="abs rule" style="top:258px"></div>
  <div class="abs rule" style="top:284px"></div>
  <div class="abs rule" style="top:312px"></div>

  <div class="footer">
    <div class="footer-item footer-phone">
      <svg width="14" height="14" viewBox="0 0 24 24"><path fill="#fff" d="M6.6 10.8a15.1 15.1 0 006.6 6.6l2.2-2.2c.3-.3.7-.4 1-.2 1.1.4 2.3.6 3.6.6.6 0 1 .4 1 1V20c0 .6-.4 1-1 1A17 17 0 013 4c0-.6.4-1 1-1h3.5c.6 0 1 .4 1 1 0 1.3.2 2.5.6 3.6.1.3 0 .7-.2 1z"/></svg>
      (555) 014-2290
    </div>
    <div class="footer-item footer-web">
      <svg width="18" height="18" viewBox="0 0 24 24" fill="none" stroke="#fff" stroke-width="1.6"><circle cx="12" cy="12" r="10"/><ellipse cx="12" cy="12" rx="4.5" ry="10"/><path d="M2 12h20M4 7h16M4 17h16"/></svg>
      www.ashworthmaplebrookinstitute.org
    </div>
    <div class="footer-item footer-address">
      <svg width="20" height="18" viewBox="0 0 24 22"><path fill="#fff" d="M12 1L1 11h3v10h6v-6h4v6h6V11h3z"/></svg>
      <span>2810 W. Alder Crest Ave,<br>#214 Fairmont, CA 90000</span>
    </div>
  </div>
</section>

</body>
</html>
```